**URGENT - Pitch Deck / Information Memorandum

We have outlined a 15-20 page "Pitch Deck" which basically gives an overview to our company. We need to make this look professional. I have attached our draft with the content we need, along with another companies example. I will also attach logos and images that can be used but please ask if more images are needed.

Industry/Entity Type

Automotive

Font styles to use
Sans Serif

Colors
ffcf3e

```html
<!DOCTYPE html>
<html lang="en">
<head>
<meta charset="utf-8">
<title>KVR Group – Information Memorandum</title>
<link href="https://fonts.googleapis.com/css2?family=Open+Sans:wght@300;400;600;700&display=swap" rel="stylesheet">
<style>
:root{
  --yellow:#ffcf3e;
  --ink:#2b2b2b;
  --grey:#6d6d6d;
  --light:#f4f4f4;
  --navy:#1f3f78;
  --dark:#232426;
  --photo-dark:#3a3d42;
  --photo-mid:#8a8d92;
  --photo-light:#c9cbce;
}
*{margin:0;padding:0;box-sizing:border-box}
html,body{width:1200px;height:2252px;overflow:hidden}
body{
  font-family:'Open Sans',Arial,sans-serif;color:var(--ink);
  background:linear-gradient(180deg,#8f9194 0%,#c8c9cb 35%,#a9abae 70%,#7c7e81 100%);
  position:relative;
}
.slide{
  position:absolute;width:540px;height:404px;background:#fff;
  border:6px solid var(--yellow);overflow:hidden;
  box-shadow:0 4px 14px rgba(0,0,0,.25);
}
.col-l{left:44px}.col-r{left:616px}
.row1{top:40px}.row2{top:482px}.row3{top:924px}.row4{top:1366px}.row5{top:1808px}
.photo{position:absolute}
.ph-dark{background:linear-gradient(135deg,#1c1d20,#4a4d53 60%,#2a2b2e)}
.ph-mid{background:linear-gradient(135deg,#5b5f66,#a3a6ab 55%,#6e7177)}
.ph-light{background:linear-gradient(135deg,#d6d7d9,#9a9da2 60%,#e4e5e6)}
.footer-url{position:absolute;right:14px;bottom:8px;font-size:8px;color:var(--grey);display:flex;align-items:center;gap:5px}
.footer-url .dot{width:8px;height:8px;border-radius:50%;background:var(--yellow)}
.kicker{font-size:13px;color:var(--grey);font-weight:400}
.title{font-size:20px;font-weight:600;color:var(--ink);line-height:1.1}
.title b{color:var(--yellow);font-weight:700}
.body-text{font-size:7.5px;line-height:1.55;color:var(--grey)}
.body-text p{margin-bottom:6px}
.sub{font-size:12px;font-weight:700;color:var(--ink);margin:8px 0 4px}
/* cover */
.cover .photo{inset:0}
.cover-title{position:absolute;left:26px;top:26px;color:#fff;font-weight:300;font-size:28px;line-height:1.05;letter-spacing:.5px}
.cover-title b{display:block;font-weight:700;font-size:34px}
.cover-rule{position:absolute;left:26px;top:110px;width:90px;height:3px;background:var(--yellow)}
.brand{position:absolute;display:flex;align-items:center;gap:8px;color:#fff;font-weight:700;font-size:22px}
.brand .mark{width:30px;height:30px;border-radius:50%;background:var(--yellow)}
.cover .brand{left:26px;bottom:52px}
.cover-bar{position:absolute;left:0;right:0;bottom:0;height:26px;background:rgba(0,0,0,.55);color:var(--yellow);font-size:9px;display:flex;align-items:center;justify-content:flex-end;padding-right:16px}
/* clients */
.clients-grid{position:absolute;left:24px;right:20px;top:238px;display:grid;grid-template-columns:repeat(3,1fr);gap:10px 16px}
.clients-grid span{font-size:10px;font-weight:600;color:var(--navy);border-bottom:1px solid #e1e1e1;padding-bottom:4px}
/* hex */
.hex{position:absolute;width:62px;height:54px}
.hex polygon{fill:#55585d}
.hex.center polygon{fill:var(--yellow)}
.hex span{position:absolute;inset:0;display:flex;align-items:center;justify-content:center;font-size:6.5px;color:#fff;font-weight:600;text-align:center}
.hex.center span{color:var(--ink)}
.fin-table{position:absolute;left:298px;top:104px;width:214px;border-collapse:collapse;font-size:7px}
.fin-table th{background:var(--ink);color:#fff;padding:6px 4px;font-weight:600}
.fin-table td{padding:9px 4px;border-bottom:1px solid #ddd;text-align:center;color:var(--grey)}
.fin-table td:first-child{text-align:left;color:var(--ink);font-weight:600}
/* columns */
.tri{position:absolute;left:18px;right:18px;top:20px;bottom:40px;display:grid;grid-template-columns:repeat(3,1fr);gap:12px}
.tri .head{background:var(--navy);color:#fff;font-size:10px;font-weight:600;text-align:center;padding:10px 0}
.tri .cell{border:1px solid #d9d9d9;border-top:none;height:62px;font-size:7px;color:var(--grey);display:flex;align-items:center;justify-content:center;text-align:center;padding:6px}
/* personnel */
.person{position:absolute;width:230px;height:58px}
.person .face{position:absolute;left:0;top:4px;width:50px;height:50px;border-radius:50%;border:3px solid var(--yellow)}
.person .name{position:absolute;left:44px;top:10px;right:0;height:18px;background:var(--dark);color:#fff;font-size:8.5px;font-weight:600;padding-left:14px;line-height:18px}
.person .role{position:absolute;left:58px;top:31px;font-size:7px;color:var(--grey)}
/* org */
.org-box{position:absolute;background:#fff;border:1px solid #cfcfcf;border-left:4px solid var(--yellow);font-size:7px;padding:4px 6px;width:120px;line-height:1.3}
.org-box b{display:block;font-size:7.5px;color:var(--ink)}
.org-box span{color:var(--grey)}
</style>
</head>
<body>

<!-- 1 Cover -->
<section class="slide col-l row1 cover">
  <div class="photo ph-dark" role="img" aria-label="Dark close-up photograph of a car wheel and hub"></div>
  <h1 class="cover-title">INFORMATION<b>MEMORANDUM</b></h1>
  <div class="cover-rule"></div>
  <div class="brand"><span class="mark"></span>KVR GROUP</div>
  <div class="cover-bar">www.kvrgroup.example</div>
</section>

<!-- 2 Intro -->
<section class="slide col-r row1">
  <div class="photo ph-mid" style="left:270px;top:0;right:0;bottom:0" role="img" aria-label="Photograph of a technician working on a vehicle panel"></div>
  <div style="position:absolute;left:22px;top:30px;width:230px">
    <div class="kicker">KVR Group</div>
    <h2 class="title">Pushing for <b>Perfection</b></h2>
    <div class="body-text" style="margin-top:14px">
      <p>KVR Group is a specialist vehicle repair business serving insurers, fleets and leasing firms across the country with fast, reliable results.</p>
      <p>We have built a reputation for quality workmanship, trained staff and a customer first approach on every job we take.</p>
      <p>Founded by experienced engineers, the group has grown steadily and now operates several divisions covering repairs, tools and training.</p>
      <p>This memorandum sets out our services, clients, people and financial performance for prospective partners.</p>
    </div>
  </div>
  <div class="footer-url"><span class="dot"></span>www.kvrgroup.example</div>
</section>

<!-- 3 Clients -->
<section class="slide col-l row2">
  <div class="photo ph-mid" style="left:0;top:0;right:0;height:170px" role="img" aria-label="Photograph of a technician inspecting a vehicle with a camera"></div>
  <div style="position:absolute;left:24px;top:190px">
    <div class="kicker">Major</div>
    <h2 class="title">Clients</h2>
  </div>
  <div class="clients-grid">
    <span>Harlow Insure</span><span>Brightmere Leasing</span><span>Norcross Fleet</span>
    <span>Vantage Motors</span><span>Pellham Cars</span><span>Oakline Rental</span>
    <span>Trident Claims</span><span>Castell Hire</span><span>Fenwood Assist</span>
  </div>
  <div class="footer-url"><span class="dot"></span>www.kvrgroup.example</div>
</section>

<!-- 4 Financial -->
<section class="slide col-r row2">
  <div style="position:absolute;left:22px;top:30px">
    <h2 class="title" style="font-weight:400;font-size:17px">Business Overview: <b style="color:var(--ink)">Financial Summery</b></h2>
  </div>
  <svg width="0" height="0" style="position:absolute"><defs><polygon id="hexshape" points="15,0 47,0 62,27 47,54 15,54 0,27"/></defs></svg>
  <div class="hex" style="left:104px;top:150px"><svg width="62" height="54"><use href="#hexshape"/></svg><span>Head Office</span></div>
  <div class="hex center" style="left:104px;top:208px"><svg width="62" height="54"><use href="#hexshape"/></svg><span>Business Divisions</span></div>
  <div class="hex" style="left:104px;top:266px"><svg width="62" height="54"><use href="#hexshape"/></svg><span>Tools</span></div>
  <div class="hex" style="left:52px;top:179px"><svg width="62" height="54"><use href="#hexshape"/></svg><span>PDR</span></div>
  <div class="hex" style="left:52px;top:237px"><svg width="62" height="54"><use href="#hexshape"/></svg><span>Training</span></div>
  <div class="hex" style="left:156px;top:179px"><svg width="62" height="54"><use href="#hexshape"/></svg><span>Repairs</span></div>
  <div class="hex" style="left:156px;top:237px"><svg width="62" height="54"><use href="#hexshape"/></svg><span>Fleet</span></div>
  <table class="fin-table">
    <tr><th>Year</th><th>2017</th><th>2018</th><th>2019</th></tr>
    <tr><td>Turnover</td><td>1.2m</td><td>1.6m</td><td>2.1m</td></tr>
    <tr><td>Gross Profit</td><td>0.4m</td><td>0.6m</td><td>0.8m</td></tr>
    <tr><td>Net Profit</td><td>0.1m</td><td>0.2m</td><td>0.3m</td></tr>
    <tr><td>Staff</td><td>18</td><td>24</td><td>31</td></tr>
  </table>
  <div class="footer-url"><span class="dot"></span>www.kvrgroup.example</div>
</section>

<!-- 5 Divisions -->
<section class="slide col-l row3">
  <div class="tri">
    <div><div class="head">Repairs</div><div class="cell">Service area: National</div><div class="cell">Length of relationship: 6 years</div><div class="cell">Status</div></div>
    <div><div class="head">Fleet</div><div class="cell">Service area: National</div><div class="cell">Length of relationship: 4 years</div><div class="cell">Status</div></div>
    <div><div class="head">Car Hire</div><div class="cell">Service area: Regional</div><div class="cell">Length of relationship: 3 years</div><div class="cell">Status</div></div>
  </div>
  <div class="footer-url"><span class="dot"></span>www.kvrgroup.example</div>
</section>

<!-- 6 PDR -->
<section class="slide col-r row3">
  <div class="photo ph-light" style="left:0;top:0;right:0;height:120px" role="img" aria-label="Photograph of a hand working on a car body panel"></div>
  <div style="position:absolute;left:22px;top:138px;width:300px">
    <div class="kicker">Services :</div>
    <h2 class="title" style="font-size:18px"><b>PDR</b></h2>
    <div class="body-text" style="margin-top:6px"><p>Paintless dent repair restores panels to factory finish without filler or paint, reducing cost and downtime for our clients.</p></div>
    <div class="sub">Intracompany Benefits</div>
    <div class="body-text"><p>Shared workshops and technicians across divisions allow fast scheduling, consistent quality and lower overheads for every job.</p></div>
  </div>
  <div class="footer-url"><span class="dot"></span>www.kvrgroup.example</div>
</section>

<!-- 7 Tools -->
<section class="slide col-l row4">
  <div class="photo ph-mid" style="left:250px;top:0;right:0;bottom:0" role="img" aria-label="Photograph of an instructor demonstrating tools in a training centre"></div>
  <div style="position:absolute;left:22px;top:36px;width:212px">
    <div class="kicker">Services :</div>
    <h2 class="title" style="font-size:18px"><b>Tools</b></h2>
    <div class="body-text" style="margin-top:8px"><p>We design and supply specialist repair tools used by our own technicians and sold to trade customers across the sector.</p><p>Every product is tested in our workshops before release.</p></div>
    <div class="sub">Intracompany Benefits</div>
    <div class="body-text"><p>Direct feedback from technicians drives new designs, keeping our tools practical and our repair teams fully equipped.</p></div>
  </div>
  <div class="footer-url"><span class="dot"></span>www.kvrgroup.example</div>
</section>

<!-- 8 Training -->
<section class="slide col-r row4">
  <div class="photo ph-light" style="left:270px;top:0;right:0;bottom:0" role="img" aria-label="Photograph of a trainer wearing glasses at a workbench"></div>
  <div style="position:absolute;left:22px;top:36px;width:228px">
    <h2 class="title" style="font-size:18px"><b>Training</b></h2>
    <div class="body-text" style="margin-top:8px"><p>Our accredited training centre runs courses for new and experienced technicians, covering repair methods, tools and safety.</p><p>Courses are delivered by senior staff with years of hands on experience.</p></div>
    <div class="sub">Intracompany Benefits</div>
    <div class="body-text"><p>Training keeps standards high across the group and gives us a steady pipeline of skilled people.</p></div>
  </div>
  <div class="footer-url"><span class="dot"></span>www.kvrgroup.example</div>
</section>

<!-- 9 Personnel -->
<section class="slide col-l row5">
  <div style="position:absolute;left:22px;top:22px">
    <div class="kicker">Key</div>
    <h2 class="title" style="font-size:18px">Personnel</h2>
  </div>
  <div class="person" style="left:26px;top:96px"><div class="face ph-mid" role="img" aria-label="Portrait photo"></div><div class="name">Daniel Marsh</div><div class="role">Managing Director</div></div>
  <div class="person" style="left:274px;top:96px"><div class="face ph-mid" role="img" aria-label="Portrait photo"></div><div class="name">Oliver Brandt</div><div class="role">Finance Director</div></div>
  <div class="person" style="left:26px;top:180px"><div class="face ph-mid" role="img" aria-label="Portrait photo"></div><div class="name">Sam Whitlock</div><div class="role">Operations Manager</div></div>
  <div class="person" style="left:274px;top:180px"><div class="face ph-mid" role="img" aria-label="Portrait photo"></div><div class="name">Priya Nandra</div><div class="role">Training Lead</div></div>
  <div class="person" style="left:26px;top:264px"><div class="face ph-mid" role="img" aria-label="Portrait photo"></div><div class="name">Leon Fairbank</div><div class="role">Tools Manager</div></div>
  <div class="person" style="left:274px;top:264px"><div class="face ph-mid" role="img" aria-label="Portrait photo"></div><div class="name">Grace Holloway</div><div class="role">Client Accounts</div></div>
  <div class="footer-url"><span class="dot"></span>www.kvrgroup.example</div>
</section>

<!-- 10 Org chart -->
<section class="slide col-r row5">
  <div style="position:absolute;left:22px;top:22px">
    <h2 class="title" style="font-size:15px;font-weight:400">KVR Group Organization Chart by Job Roles</h2>
  </div>
  <svg style="position:absolute;left:0;top:0" width="528" height="392">
    <g stroke="#ffcf3e" stroke-width="2" fill="none">
      <path d="M150 88 V350"/>
      <path d="M150 88 H300 V350"/>
      <path d="M150 130 H160 M150 172 H160 M150 214 H160 M150 256 H160 M150 298 H160 M150 340 H160"/>
      <path d="M300 110 H320 M300 160 H320 M300 210 H320 M300 260 H320 M300 310 H320"/>
    </g>
  </svg>
  <div class="org-box" style="left:40px;top:70px;width:110px"><b>Tom Keller</b><span>Group Director</span></div>
  <div class="org-box" style="left:160px;top:118px"><b>Ruth Aldine</b><span>Office Manager</span></div>
  <div class="org-box" style="left:160px;top:160px"><b>Mark Enfield</b><span>Repairs Lead</span></div>
  <div class="org-box" style="left:160px;top:202px"><b>Carl Dorsey</b><span>Fleet Lead</span></div>
  <div class="org-box" style="left:160px;top:244px"><b>Nina Sutter</b><span>Accounts</span></div>
  <div class="org-box" style="left:160px;top:286px"><b>Ian Royce</b><span>Workshop Lead</span></div>
  <div class="org-box" style="left:160px;top:328px"><b>Jo Lambert</b><span>Administration</span></div>
  <div class="org-box" style="left:320px;top:98px;width:110px"><b>Technician</b><span>PDR Team</span></div>
  <div class="org-box" style="left:320px;top:148px;width:110px"><b>Technician</b><span>Repairs Team</span></div>
  <div class="org-box" style="left:320px;top:198px;width:110px"><b>Trainer</b><span>Training Centre</span></div>
  <div class="org-box" style="left:320px;top:248px;width:110px"><b>Sales</b><span>Tools Division</span></div>
  <div class="org-box" style="left:320px;top:298px;width:110px"><b>Driver</b><span>Fleet Support</span></div>
  <div class="footer-url"><span class="dot"></span>www.kvrgroup.example</div>
</section>

</body>
</html>
```